Icons for an Inspections System (codenamed Pemberlow)

We are developing a new system to manage inspections (ie an inspector goes out to a "centre" to perform an inspection which covers say 100 questions/factors).
The home page is adopting Windows 8 style boxes and we are looking for icons for the top left corner of each box.
All icons are to be white and 40x25 pixels. They are all to be fairly simple in design. I am not looking for anything radically new/different - just something simple and straightforward.
MAIN ITEMS
We need icons for the following main functions:
Centres
Inspectors
Inspections
Self-Inspections
Certificates
Reports
Templates
Categories
Factors
NEW RECORDS
A version of each of the above but with a small asterisk/star shape in one corner to indicate "new". For example: New Centre, New Inspector etc
OTHER ICONS
We also need the same style of icons for the following:
Configuration
Change Password
Sign Out
Other info:
Centres: a centre could be a building or a site where an inspection takes place
Inspector: an inspector is a man or a woman! I was thinking maybe a magnifying glass could be a good icon but I'm open to other ideas
Certificates: when a centre passes an inspection they get a certificate
Templates: these are groups of factors (like questions) to be used on an inspection; they are grouped into categories

Target Market(s)
Trade associations who are looking to perform inspections on members
Look and feel
Each slider illustrates characteristics of the customer's brand and the style your logo design should communicate.

```html
<!DOCTYPE html>
<html lang="en">
<head>
<meta charset="utf-8">
<title>Pemberlow — Home Icons</title>
<link rel="stylesheet" href="https://fonts.googleapis.com/css2?family=Open+Sans:wght@300;400&display=swap">
<style>
  :root {
    --page-bg: #ffffff;
    --tile-bg: #666666;
    --tile-ink: #ffffff;
    --tile-detail: #666666;
    --tile-soft: #9a9a9a;
    --label-ink: #bcbcbc;
    --rule: #c9c9c9;
  }
  html, body {
    margin: 0;
    padding: 0;
    width: 1033px;
    height: 1200px;
    overflow: hidden;
    background: var(--page-bg);
  }
  .menu-board {
    position: relative;
    width: 1033px;
    height: 1200px;
    font-family: "Open Sans", Arial, sans-serif;
  }
  .rule-v, .rule-h {
    position: absolute;
    background: var(--rule);
  }
  .rule-v { width: 3px; top: 33px; height: 1137px; }
  .rule-h { height: 3px; left: 21px; width: 996px; }
  .menu-item {
    position: absolute;
    width: 260px;
    text-align: center;
  }
  .menu-tile {
    display: block;
    width: 195px;
    height: 120px;
    margin: 0 auto;
  }
  .menu-label {
    display: block;
    margin-top: 14px;
    color: var(--label-ink);
    font-weight: 300;
    font-size: 31px;
    line-height: 32px;
    letter-spacing: 0.2px;
  }
  .col-1 { left: 73px; }
  .col-2 { left: 366px; }
  .col-3 { left: 667px; }
  .row-1 { top: 69px; }
  .row-2 { top: 313px; }
  .row-3 { top: 565px; }
  .row-4 { top: 923px; }
  .col-2.row-4 { left: 366px; }
</style>
</head>
<body>
<main class="menu-board">
  <div class="rule-v" style="left:354px"></div>
  <div class="rule-v" style="left:645px"></div>
  <div class="rule-h" style="top:279px"></div>
  <div class="rule-h" style="top:528px"></div>
  <div class="rule-h" style="top:877px"></div>

  <!-- Centres -->
  <div class="menu-item col-1 row-1">
    <svg class="menu-tile" viewBox="0 0 130 80">
      <rect width="130" height="80" rx="2" fill="var(--tile-bg)"/>
      <path d="M18 70 V40 H34 V34 H64 V14 H108 V70 Z" fill="var(--tile-ink)"/>
      <g fill="var(--tile-detail)">
        <rect x="72" y="22" width="6" height="6"/><rect x="83" y="22" width="6" height="6"/><rect x="94" y="22" width="6" height="6"/>
        <rect x="72" y="34" width="6" height="6"/><rect x="83" y="34" width="6" height="6"/><rect x="94" y="34" width="6" height="6"/>
        <rect x="72" y="46" width="6" height="6"/><rect x="83" y="46" width="6" height="6"/><rect x="94" y="46" width="6" height="6"/>
        <rect x="24" y="50" width="6" height="6"/><rect x="36" y="50" width="6" height="6"/><rect x="48" y="50" width="6" height="6"/>
      </g>
      <rect x="12" y="70" width="104" height="4" fill="var(--tile-ink)"/>
    </svg>
    <span class="menu-label">Centres</span>
  </div>

  <!-- Inspectors -->
  <div class="menu-item col-2 row-1">
    <svg class="menu-tile" viewBox="0 0 130 80">
      <rect width="130" height="80" rx="2" fill="var(--tile-bg)"/>
      <rect x="42" y="8" width="46" height="64" rx="6" fill="var(--tile-soft)" role="img" aria-label="Inspector figure icon"/>
    </svg>
    <span class="menu-label">Inspectors</span>
  </div>

  <!-- Inspections -->
  <div class="menu-item col-3 row-1">
    <svg class="menu-tile" viewBox="0 0 130 80">
      <rect width="130" height="80" rx="2" fill="var(--tile-bg)"/>
      <circle cx="78" cy="32" r="16" fill="none" stroke="var(--tile-ink)" stroke-width="6"/>
      <line x1="65" y1="45" x2="48" y2="64" stroke="var(--tile-ink)" stroke-width="10" stroke-linecap="round"/>
    </svg>
    <span class="menu-label">Inspections</span>
  </div>

  <!-- Self-Inspections -->
  <div class="menu-item col-1 row-2">
    <svg class="menu-tile" viewBox="0 0 130 80">
      <rect width="130" height="80" rx="2" fill="var(--tile-bg)"/>
      <circle cx="58" cy="42" r="25" fill="none" stroke="var(--tile-ink)" stroke-width="5"/>
      <polyline points="45,42 56,53 104,10" fill="none" stroke="var(--tile-ink)" stroke-width="7" stroke-linejoin="round"/>
    </svg>
    <span class="menu-label">Self-Inspections</span>
  </div>

  <!-- Certificates -->
  <div class="menu-item col-2 row-2">
    <svg class="menu-tile" viewBox="0 0 130 80">
      <rect width="130" height="80" rx="2" fill="var(--tile-bg)"/>
      <rect x="36" y="8" width="50" height="66" fill="var(--tile-ink)"/>
      <g fill="var(--tile-soft)">
        <rect x="42" y="16" width="38" height="3"/>
        <rect x="42" y="26" width="30" height="7"/>
        <rect x="42" y="38" width="28" height="3"/>
        <rect x="42" y="45" width="16" height="3"/>
      </g>
      <circle cx="84" cy="56" r="14" fill="var(--tile-ink)" stroke="var(--tile-soft)" stroke-width="2" stroke-dasharray="3 2"/>
    </svg>
    <span class="menu-label">Certificates</span>
  </div>

  <!-- Reports -->
  <div class="menu-item col-3 row-2">
    <svg class="menu-tile" viewBox="0 0 130 80">
      <rect width="130" height="80" rx="2" fill="var(--tile-bg)"/>
      <rect x="58" y="8" width="34" height="50" fill="var(--tile-ink)" stroke="var(--tile-bg)" stroke-width="2"/>
      <rect x="50" y="14" width="34" height="52" fill="var(--tile-ink)" stroke="var(--tile-bg)" stroke-width="2"/>
      <rect x="42" y="20" width="34" height="54" fill="var(--tile-ink)" stroke="var(--tile-bg)" stroke-width="2"/>
      <g fill="var(--tile-bg)">
        <rect x="48" y="28" width="22" height="2"/><rect x="48" y="34" width="22" height="2"/>
        <rect x="48" y="40" width="22" height="2"/><rect x="48" y="46" width="22" height="2"/>
        <rect x="48" y="52" width="22" height="2"/><rect x="48" y="58" width="22" height="2"/>
      </g>
    </svg>
    <span class="menu-label">Reports</span>
  </div>

  <!-- Templates -->
  <div class="menu-item col-1 row-3">
    <svg class="menu-tile" viewBox="0 0 130 80">
      <rect width="130" height="80" rx="2" fill="var(--tile-bg)"/>
      <path d="M44 10 H84 V58 L72 70 H44 Z" fill="none" stroke="var(--tile-ink)" stroke-width="5"/>
      <polygon points="84,58 72,58 72,70" fill="var(--tile-ink)"/>
      <polygon points="64,32 66.6,38.5 73.5,39 68.2,43.4 70,50 64,46.3 58,50 59.8,43.4 54.5,39 61.4,38.5" fill="var(--tile-ink)"/>
    </svg>
    <span class="menu-label">Templates</span>
  </div>

  <!-- Categories -->
  <div class="menu-item col-2 row-3">
    <svg class="menu-tile" viewBox="0 0 130 80">
      <rect width="130" height="80" rx="2" fill="var(--tile-bg)"/>
      <g fill="none" stroke="var(--tile-ink)" stroke-width="2">
        <line x1="65" y1="24" x2="65" y2="36"/>
        <line x1="35" y1="36" x2="95" y2="36"/>
        <line x1="35" y1="36" x2="35" y2="48"/>
        <line x1="95" y1="36" x2="95" y2="48"/>
      </g>
      <rect x="54" y="6" width="22" height="18" fill="var(--tile-ink)"/>
      <rect x="24" y="48" width="22" height="18" fill="var(--tile-ink)"/>
      <rect x="84" y="48" width="22" height="18" fill="var(--tile-ink)"/>
      <g fill="var(--tile-soft)">
        <rect x="58" y="10" width="14" height="10"/>
        <rect x="28" y="52" width="14" height="10"/>
        <rect x="88" y="52" width="14" height="10"/>
      </g>
    </svg>
    <span class="menu-label">Categories</span>
  </div>

  <!-- Factors -->
  <div class="menu-item col-3 row-3">
    <svg class="menu-tile" viewBox="0 0 130 80">
      <rect width="130" height="80" rx="2" fill="var(--tile-bg)"/>
      <rect x="42" y="6" width="48" height="70" fill="var(--tile-ink)"/>
      <g fill="none" stroke="var(--tile-bg)" stroke-width="2">
        <circle cx="42" cy="22" r="3"/><circle cx="42" cy="40" r="3"/><circle cx="42" cy="58" r="3"/>
        <line x1="72" y1="24" x2="84" y2="24"/><line x1="72" y1="42" x2="84" y2="42"/><line x1="72" y1="60" x2="84" y2="60"/>
      </g>
      <g fill="none" stroke="var(--tile-bg)" stroke-width="5" stroke-linejoin="round">
        <polyline points="52,20 58,26 70,12"/>
        <polyline points="52,38 58,44 70,30"/>
        <polyline points="52,56 58,62 70,48"/>
      </g>
    </svg>
    <span class="menu-label">Factors</span>
  </div>

  <!-- Configuration -->
  <div class="menu-item col-1 row-4">
    <svg class="menu-tile" viewBox="0 0 130 80">
      <rect width="130" height="80" rx="2" fill="var(--tile-bg)"/>
      <g fill="var(--tile-ink)" transform="translate(65 40)">
        <circle r="20"/>
        <rect x="-6" y="-28" width="12" height="56" rx="2"/>
        <rect x="-6" y="-28" width="12" height="56" rx="2" transform="rotate(45)"/>
        <rect x="-6" y="-28" width="12" height="56" rx="2" transform="rotate(90)"/>
        <rect x="-6" y="-28" width="12" height="56" rx="2" transform="rotate(135)"/>
      </g>
      <circle cx="65" cy="40" r="8" fill="var(--tile-bg)"/>
      <circle cx="65" cy="40" r="5" fill="var(--tile-ink)"/>
    </svg>
    <span class="menu-label">Configuration</span>
  </div>

  <!-- Change Password -->
  <div class="menu-item col-2 row-4">
    <svg class="menu-tile" viewBox="0 0 130 80">
      <rect width="130" height="80" rx="2" fill="var(--tile-bg)"/>
      <g fill="none" stroke="var(--tile-ink)" stroke-width="2.5">
        <path d="M46 30 A 22 22 0 0 1 82 20"/>
        <path d="M84 50 A 22 22 0 0 1 48 60"/>
      </g>
      <polygon points="86,14 88,26 77,22" fill="var(--tile-ink)"/>
      <polygon points="44,66 42,54 53,58" fill="var(--tile-ink)"/>
      <circle cx="58" cy="34" r="10" fill="var(--tile-ink)"/>
      <circle cx="56" cy="32" r="3" fill="var(--tile-bg)"/>
      <path d="M64 40 L78 54 L74 58 L71 55 L68 58 L65 55 L68 52 L60 44 Z" fill="var(--tile-ink)"/>
    </svg>
    <span class="menu-label">Change<br>Password</span>
  </div>

  <!-- Sign Out -->
  <div class="menu-item col-3 row-4">
    <svg class="menu-tile" viewBox="0 0 130 80">
      <rect width="130" height="80" rx="2" fill="var(--tile-bg)"/>
      <path d="M53 22 A 22 22 0 1 0 77 22" fill="none" stroke="var(--tile-ink)" stroke-width="6" stroke-linecap="round"/>
      <line x1="65" y1="12" x2="65" y2="40" stroke="var(--tile-ink)" stroke-width="6" stroke-linecap="round"/>
    </svg>
    <span class="menu-label">Sign Out</span>
  </div>
</main>
</body>
</html>
```